Stonebay Towing Business Card

Towing
Accident towing
Mechanical breakdown
Insurance, salvage and recovery
4wd off road towing
Light & Heavy towing
8347 2516
24 hour business 7 days

Logo can be whole size on front

Industry/Entity Type

Towing/ transport

Contact Information for Business Card

The above

```html
<!DOCTYPE html>
<html lang="en">
<head>
<meta charset="utf-8">
<title>Stonebay Towing – Business Card</title>
<link href="https://fonts.googleapis.com/css2?family=Roboto:wght@400;500;700&family=Roboto+Condensed:wght@700&display=swap" rel="stylesheet">
<style>
  :root {
    --bg: #3a3a3a;
    --card-dark: #2b2b2c;
    --card-light: #ffffff;
    --red: #d91f26;
    --ink: #111111;
    --grey-text: #8a8a8a;
    --body-text: #3c3c3c;
    --rule: #d6d6d6;
    --dark-logo: #555557;
    --white: #ffffff;
  }
  * { margin: 0; padding: 0; box-sizing: border-box; }
  html, body { width: 1200px; height: 689px; overflow: hidden; }
  body {
    background: var(--bg);
    font-family: "Roboto", Arial, sans-serif;
    position: relative;
  }
  .card {
    position: absolute;
    top: 185px;
    width: 540px;
    height: 320px;
    border-radius: 18px;
    overflow: hidden;
  }
  /* Back side */
  .card-back { left: 40px; background: var(--card-dark); }
  .card-back .brand {
    position: absolute; left: 0; right: 0; top: 78px;
    text-align: center;
    font-weight: 700; font-size: 46px;
    color: var(--dark-logo);
    letter-spacing: 0.5px;
  }
  .services {
    position: absolute; left: 0; right: 0; top: 200px;
    text-align: center;
    color: var(--white);
    font-size: 15px; line-height: 24px;
  }
  .services .dot {
    display: inline-block; width: 7px; height: 7px;
    border-radius: 50%; background: var(--red);
    margin: 0 8px; vertical-align: middle;
  }
  /* Front side */
  .card-front { left: 620px; background: var(--card-light); }
  .card-front .brand {
    position: absolute; right: 34px; top: 40px;
    font-weight: 700; font-size: 36px;
    color: var(--red);
  }
  .card-front .rule {
    position: absolute; left: 34px; right: 34px; top: 112px;
    height: 1px; background: var(--rule);
  }
  .hours {
    position: absolute; right: 34px; top: 128px;
    display: flex; align-items: center; gap: 8px;
    font-size: 14px; color: var(--body-text);
  }
  .person { position: absolute; left: 34px; top: 150px; }
  .person .name {
    font-family: "Roboto Condensed", Arial, sans-serif;
    font-weight: 700; font-size: 28px; color: var(--red);
    letter-spacing: 0.5px;
  }
  .person .role { font-size: 14px; color: var(--grey-text); margin-top: 2px; }
  .person .divider { width: 200px; height: 1px; background: var(--rule); margin: 10px 0; }
  .contact { list-style: none; font-size: 15px; color: var(--body-text); }
  .contact li { display: flex; align-items: center; gap: 9px; line-height: 22px; }
  .bands { position: absolute; left: 0; bottom: 0; width: 540px; height: 80px; }
  .web {
    position: absolute; right: 26px; bottom: 22px;
    color: var(--white); font-size: 14px; font-weight: 500;
  }
</style>
</head>
<body>

<section class="card card-back" aria-label="Card back">
  <div class="brand">Stonebay Towing</div>
  <div class="services">
    Towing<span class="dot"></span>Accident towing<span class="dot"></span>Mechanical breakdown<br>
    Insurance, salvage &amp; recovery<span class="dot"></span>4wd off road towing<span class="dot"></span>Light &amp; Heavy towing
  </div>
</section>

<section class="card card-front" aria-label="Card front">
  <div class="brand">Stonebay Towing</div>
  <div class="rule"></div>

  <div class="hours">
    <svg width="28" height="28" viewBox="0 0 28 28" aria-hidden="true">
      <path d="M24 9 A11 11 0 1 0 25 14" fill="none" stroke="var(--red)" stroke-width="2"/>
      <path d="M21 6 L25 9 L21 12" fill="none" stroke="var(--red)" stroke-width="2"/>
      <text x="14" y="17" text-anchor="middle" font-size="8" font-weight="700" fill="var(--red)" font-family="Roboto, Arial, sans-serif">24/7</text>
    </svg>
    <span>24 hour business 7 days</span>
  </div>

  <div class="person">
    <div class="name">ALEX CARTER</div>
    <div class="role">President</div>
    <div class="divider"></div>
    <ul class="contact">
      <li>
        <svg width="12" height="12" viewBox="0 0 24 24" aria-hidden="true"><path fill="var(--red)" d="M6.6 10.8a15 15 0 0 0 6.6 6.6l2.2-2.2a1 1 0 0 1 1-.25 11.4 11.4 0 0 0 3.6.57 1 1 0 0 1 1 1V20a1 1 0 0 1-1 1A17 17 0 0 1 3 4a1 1 0 0 1 1-1h3.5a1 1 0 0 1 1 1c0 1.25.2 2.45.57 3.6a1 1 0 0 1-.25 1z"/></svg>
        8347 2516
      </li>
      <li>
        <svg width="12" height="10" viewBox="0 0 24 18" aria-hidden="true"><rect width="24" height="18" rx="2" fill="var(--red)"/><path d="M1 2 L12 10 L23 2" fill="none" stroke="#fff" stroke-width="2"/></svg>
        info@stonebaytowing.com
      </li>
    </ul>
  </div>

  <svg class="bands" viewBox="0 0 540 80" aria-hidden="true">
    <path d="M0 62 L300 50 Q312 50 316 44 L330 36 L540 36 L540 80 L0 80 Z" fill="var(--red)"/>
    <path d="M0 66 L296 56 Q306 56 310 50 L318 46 L0 60 Z" fill="var(--ink)"/>
  </svg>
  <div class="web">www.stonebaytowing.com</div>
</section>

</body>
</html>
```